Business Card Design Project

Business card design for an IT Service company. A logo has already been created in a different contest and has been attached to this project. Ideally we're looking for a double sided business card that matches the look and feel of our newly created logo.

We're open to creativity if you feel a tag line is needed such as "IT Services and Application Development". We're open to really and look and feel - even single sided business cards if you feel you have something that's a great idea.

Last thought here - I'm not sure how it'll look but maybe a two tone card? One side dark blue and the other side white? Don't limit the design submissions to this tho - just curious if it would look good

Nothing too busy please - simple... Thank you and happy designing!

Target Market(s)

Businesses that require IT Services and support for hosted services, technical consultation, web design.

Industry/Entity Type

Business

Font styles to use
Sans Serif

Requirements
Must have
• Use the colors provided in the logo (see attachment) or additional colors that compliment
Must have the following contact info (not necessarily in this order):
- Alan Fisk
- Founding Partner
- afisk@quillbarrow.example
- 555-382-1946
- www.quillbarrow.example

```html
<!DOCTYPE html>
<html lang="en">
<head>
<meta charset="utf-8">
<title>Quillbarrow – Business Card</title>
<link rel="stylesheet" href="https://fonts.googleapis.com/css2?family=Source+Sans+3:wght@400;600;700&display=swap">
<style>
  :root {
    --navy: #262a36;
    --green: #608b24;
    --paper-top: #f1f1ef;
    --paper-bottom: #fafafa;
    --ink: #262a36;
    --white: #ffffff;
  }
  html, body {
    margin: 0;
    padding: 0;
    overflow: hidden;
  }
  body {
    width: 1200px;
    height: 720px;
  }
  .card {
    position: relative;
    width: 1200px;
    height: 720px;
    overflow: hidden;
    background: linear-gradient(180deg, var(--paper-top) 0%, var(--paper-bottom) 100%);
    font-family: "Source Sans 3", sans-serif;
    color: var(--ink);
  }
  .band-left {
    position: absolute;
    left: 0;
    top: 305px;
    width: 80px;
    height: 113px;
    background: var(--navy);
  }
  .band-right {
    position: absolute;
    left: 600px;
    top: 305px;
    width: 600px;
    height: 113px;
    background: var(--navy);
  }
  .brand {
    position: absolute;
    left: 108px;
    top: 318px;
  }
  .brand-row {
    display: flex;
    align-items: center;
    gap: 16px;
  }
  .brand-mark {
    width: 58px;
    height: 58px;
    background: var(--green);
  }
  .brand-name {
    font-size: 76px;
    font-weight: 700;
    line-height: 1;
    color: var(--navy);
    letter-spacing: -1px;
  }
  .tagline {
    margin-top: 8px;
    margin-left: 10px;
    font-size: 15.5px;
    font-weight: 600;
    letter-spacing: 2.3px;
    color: var(--green);
    text-transform: uppercase;
  }
  .person {
    position: absolute;
    left: 641px;
    top: 318px;
    color: var(--white);
  }
  .person-name {
    font-size: 37px;
    font-weight: 600;
    letter-spacing: 1.5px;
    line-height: 1;
    margin: 0;
  }
  .person-title {
    font-size: 23px;
    font-weight: 400;
    letter-spacing: 0.5px;
    margin: 10px 0 0;
  }
  .contacts {
    position: absolute;
    left: 596px;
    top: 478px;
    margin: 0;
    padding: 0;
    list-style: none;
  }
  .contact {
    display: flex;
    align-items: center;
    height: 34px;
    margin-bottom: 8px;
    font-size: 24px;
    letter-spacing: 0.4px;
    color: var(--ink);
  }
  .contact-icon {
    width: 34px;
    height: 34px;
    margin-right: 13px;
    flex: none;
  }
</style>
</head>
<body>
<main class="card">
  <div class="band-left"></div>
  <div class="band-right"></div>

  <div class="brand">
    <div class="brand-row">
      <div class="brand-mark"></div>
      <div class="brand-name">Quillbarrow</div>
    </div>
    <div class="tagline">IT Services and Application Management</div>
  </div>

  <div class="person">
    <h1 class="person-name">ALAN FISK</h1>
    <p class="person-title">Founding Partner</p>
  </div>

  <ul class="contacts">
    <li class="contact">
      <svg class="contact-icon" viewBox="0 0 34 34" aria-hidden="true">
        <rect width="34" height="34" fill="var(--green)"/>
        <circle cx="17" cy="17" r="10" fill="none" stroke="#fff" stroke-width="2"/>
        <ellipse cx="17" cy="17" rx="4.5" ry="10" fill="none" stroke="#fff" stroke-width="1.6"/>
        <line x1="7" y1="17" x2="27" y2="17" stroke="#fff" stroke-width="1.6"/>
      </svg>
      www.quillbarrow.example
    </li>
    <li class="contact">
      <svg class="contact-icon" viewBox="0 0 34 34" aria-hidden="true">
        <rect width="34" height="34" fill="var(--green)"/>
        <rect x="7" y="10" width="20" height="14" fill="none" stroke="#fff" stroke-width="2"/>
        <polyline points="7,10 17,18 27,10" fill="none" stroke="#fff" stroke-width="2"/>
      </svg>
      afisk@quillbarrow.example
    </li>
    <li class="contact">
      <svg class="contact-icon" viewBox="0 0 34 34" aria-hidden="true">
        <rect width="34" height="34" fill="var(--green)"/>
        <path d="M7 14 Q17 6 27 14 L24 17 L21 14 L13 14 L10 17 Z" fill="#fff"/>
        <path d="M11 18 L23 18 L26 26 L8 26 Z" fill="#fff"/>
        <circle cx="17" cy="22" r="2.4" fill="var(--green)"/>
      </svg>
      555-382-1946 / 555-382-1947
    </li>
    <li class="contact">
      <svg class="contact-icon" viewBox="0 0 34 34" aria-hidden="true">
        <rect width="34" height="34" fill="var(--green)"/>
        <polyline points="13,9 21,17 13,25" fill="none" stroke="#fff" stroke-width="4"/>
      </svg>
      48 Harlow Lane, Eastgate, Fairview
    </li>
  </ul>
</main>
</body>
</html>
```